Business Card Design

New business card design

Target Market(s)

Residential & Commercial Property Managers

Industry/Entity Type

Plumbing Services

Contact Information for Business Card

Name - Tom Brereton, title - Director, Phone Number - 0431 862 517, email - tom@rvk-plumbing.com.au, Company ABN - 73 512 938 204,

Font styles to use
Sans Serif

Colors
0054AA
0677BA
7BADD7
CADEEF
E8F1F8

```html
<!DOCTYPE html>
<html lang="en">
<head>
<meta charset="utf-8">
<title>RVK Plumbing Services – Business Card</title>
<link rel="stylesheet" href="https://fonts.googleapis.com/css2?family=Montserrat:wght@400;500;700&display=swap">
<style>
  :root {
    --backdrop: #e4e2e3;
    --card-light: #ffffff;
    --card-dark: #1e232c;
    --ink: #1f232b;
    --brand-blue: #0677ba;
    --name-light: #7badd7;
  }
  * { box-sizing: border-box; margin: 0; padding: 0; }
  html, body {
    width: 1200px; height: 1108px; overflow: hidden;
    background: var(--backdrop);
    font-family: "Montserrat", sans-serif;
    color: var(--ink);
  }
  .canvas { position: relative; width: 1200px; height: 1108px; }

  .card { position: absolute; width: 740px; height: 444px; }
  .card--front { left: 236px; top: 61px; background: var(--card-light); }
  .card--back { left: 235px; top: 580px; background: var(--card-dark); }

  .company-name {
    position: absolute; text-align: center; white-space: nowrap;
    font-weight: 500; line-height: 1;
  }
  .card--front .company-name {
    left: 50px; top: 228px; width: 310px;
    font-size: 26px; color: var(--ink);
  }
  .card--back .company-name {
    left: 0; top: 228px; width: 740px;
    font-size: 52px; color: var(--name-light);
  }

  .divider {
    position: absolute; left: 373px; top: 149px;
    width: 2px; height: 186px; background: var(--ink);
  }

  .contact { position: absolute; left: 393px; top: 146px; }
  .contact__name { font-size: 27px; font-weight: 700; line-height: 1.2; }
  .contact__title { font-size: 16px; font-weight: 400; margin-top: 2px; }
  .contact__list { list-style: none; margin-top: 18px; }
  .contact__item {
    display: flex; align-items: center; gap: 10px;
    font-size: 15.5px; height: 31px;
  }
  .contact__icon { width: 17px; height: 17px; fill: var(--ink); flex: none; }
  .contact__abn { font-size: 15.5px; margin-top: 4px; }
  .contact__abn strong { font-weight: 700; }

  .edge-accent {
    position: absolute; right: 0; bottom: 0; width: 385px; height: 2px;
    background: var(--brand-blue);
  }
</style>
</head>
<body>
<main class="canvas">

  <section class="card card--front" aria-label="Business card front">
    <p class="company-name">RVK Plumbing Services</p>

    <div class="divider"></div>

    <div class="contact">
      <h1 class="contact__name">Tom Brereton</h1>
      <p class="contact__title">Director</p>
      <ul class="contact__list">
        <li class="contact__item">
          <svg class="contact__icon" viewBox="0 0 24 24" aria-hidden="true"><path d="M6.6 10.8a15.1 15.1 0 0 0 6.6 6.6l2.2-2.2a1 1 0 0 1 1-.25 11.4 11.4 0 0 0 3.6.57 1 1 0 0 1 1 1V20a1 1 0 0 1-1 1A17 17 0 0 1 3 4a1 1 0 0 1 1-1h3.5a1 1 0 0 1 1 1c0 1.25.2 2.45.57 3.57a1 1 0 0 1-.25 1z"/></svg>
          <span>0431 862 517</span>
        </li>
        <li class="contact__item">
          <svg class="contact__icon" viewBox="0 0 24 24" aria-hidden="true"><path d="M4 7h16l-8 6z"/><path d="M4 9l8 6 8-6v8H4z"/></svg>
          <span>tom@rvk-plumbing.com.au</span>
        </li>
        <li class="contact__item">
          <svg class="contact__icon" viewBox="0 0 24 24" aria-hidden="true"><circle cx="12" cy="12" r="9" fill="none" stroke="#1f232b" stroke-width="2.2"/><path d="M3 12h18M12 3c-3 3-3 15 0 18M12 3c3 3 3 15 0 18" fill="none" stroke="#1f232b" stroke-width="1.6"/></svg>
          <span>www.rvk-plumbing.com.au</span>
        </li>
      </ul>
      <p class="contact__abn"><strong>ABN</strong> - 73 512 938 204,</p>
    </div>
  </section>

  <section class="card card--back" aria-label="Business card back">
    <p class="company-name">RVK Plumbing Services</p>
    <div class="edge-accent"></div>
  </section>

</main>
</body>
</html>
```